Wedding Photography business card

I need a business card made for a wedding photography business. Formal, unique, i like dark colors maybe black, white, gray, deep blue, silver. Sharp.

This is an idea i have i don't know if it would work.
Think Palm Beach, florida

work in mirror mode in your design program, Just an idea

Front side:
feminine, classy maybe white from wedding dress,
script, elegant,

back side:
masculine, black from tux, symbolizing strength, power,
serif

RV Photography
(555) 214-3097
www.ruthvlenses.example

Target Market(s)

upscale Weddings, targeting bride and groom

Industry/Entity Type

Wedding

Font styles to use
Serif
Script

Colors

Designer to choose colors to be used in the design.

Requirements
Must have
• both sides match somehow

```html
<!DOCTYPE html>
<html lang="en">
<head>
<meta charset="utf-8">
<title>RV Photography – Business Cards</title>
<link rel="stylesheet" href="https://fonts.googleapis.com/css2?family=Crimson+Text:wght@400;700&display=swap">
<style>
  :root {
    --backdrop: #404040;
    --card: #ffffff;
    --ink: #000000;
    --paper-text: #ffffff;
  }
  * { margin: 0; padding: 0; box-sizing: border-box; }
  html, body {
    width: 1200px;
    height: 1000px;
    overflow: hidden;
    background: var(--backdrop);
  }
  .canvas {
    position: relative;
    width: 1200px;
    height: 1000px;
    font-family: "Crimson Text", Georgia, serif;
  }
  .card {
    position: absolute;
    width: 295px;
    height: 532px;
    background: var(--card);
    overflow: hidden;
  }
  .card--front-name { left: 95px; top: 202px; }
  .card--front-monogram { left: 463px; top: 203px; }
  .card--back { left: 821px; top: 203px; }

  .tie-area {
    position: absolute;
    left: 96px;
    top: 0;
    width: 103px;
    height: 532px;
    background: var(--ink);
  }
  .gown-area {
    position: absolute;
    left: 0;
    top: 0;
    width: 100%;
    height: 370px;
    background: linear-gradient(180deg, var(--ink) 0%, #5a5a5a 55%, var(--card) 100%);
  }

  .tie-label {
    position: absolute;
    left: 0;
    width: 100%;
    text-align: center;
    color: var(--paper-text);
    line-height: 1;
  }
  .tie-label__name {
    top: 444px;
    font-size: 15px;
    font-weight: 700;
    letter-spacing: 1.2px;
  }
  .tie-label__monogram {
    top: 440px;
    font-size: 20px;
    font-weight: 700;
    letter-spacing: 1px;
  }
  .tie-label__sub {
    top: 462px;
    font-size: 12px;
    letter-spacing: 0.9px;
  }
  .card--front-monogram .tie-label__sub { top: 464px; }

  .contact {
    position: absolute;
    left: 0;
    top: 408px;
    width: 100%;
    text-align: center;
    color: var(--ink);
    line-height: 1;
  }
  .contact__name { font-size: 14.5px; letter-spacing: 1.3px; }
  .contact__role { font-size: 14.5px; letter-spacing: 0.5px; margin-top: 3px; }
  .contact__phone { font-size: 12px; letter-spacing: 0.4px; margin-top: 5px; }
  .contact__web { font-size: 11px; letter-spacing: 0.4px; margin-top: 6px; }
</style>
</head>
<body>
<main class="canvas">

  <section class="card card--front-name">
    <div class="tie-area" role="img" aria-label="Black necktie illustration"></div>
    <p class="tie-label tie-label__name">Vance</p>
    <p class="tie-label tie-label__sub">Photography</p>
  </section>

  <section class="card card--front-monogram">
    <div class="tie-area" role="img" aria-label="Black necktie illustration"></div>
    <p class="tie-label tie-label__monogram">RV</p>
    <p class="tie-label tie-label__sub">Photography</p>
  </section>

  <section class="card card--back">
    <div class="gown-area" role="img" aria-label="Black and white wedding gown silhouette illustration"></div>
    <div class="contact">
      <p class="contact__name">Ruth Vance</p>
      <p class="contact__role">wedding photography</p>
      <p class="contact__phone">(555) 214-3097</p>
      <p class="contact__web">www.ruthvlenses.example</p>
    </div>
  </section>

</main>
</body>
</html>
```